Velmora Works Brochure Design Project

Our company requires a brochure for promoting our Corporate Training business.

Please use data from Corporate training brochure doc.

Dear Designers,

We have added new corporate brochure document into the project. Use this data to finish up your brochure.

Thanks,

Omar deswick

Reason: We have recently finalised the data that will go into the corporate brochure.

Reason: To get more better designs

Target Market(s)

Training Managers / Business Managers / Hiring Managers

Industry/Entity Type

Training

Requirements
Must have
• Corporate and Professional Look

```html
<!DOCTYPE html>
<html lang="en">
<head>
<meta charset="utf-8">
<title>Corporate Training Brochure</title>
<link rel="stylesheet" href="https://fonts.googleapis.com/css2?family=Open+Sans:wght@300;400;600;700;800&family=Arimo:wght@400;700&display=swap">
<style>
  :root {
    --frame: #3b1a4d;
    --frame-edge: #f4f2f6;
    --panel: #3e4041;
    --panel-deep: #393b3c;
    --tab-top: #676869;
    --tab-bottom: #444647;
    --rule: #5a5c5d;
    --text: #ffffff;
    --text-soft: #d9d9d9;
    --text-muted: #9a9a9a;
    --tab-sub: #a9a9a9;
    --accent: #6cc3e6;
    --photo-room-a: #b9c0c6;
    --photo-room-b: #55606b;
    --photo-sky-a: #e4e8ee;
    --photo-sky-b: #8d98a6;
  }
  * { box-sizing: border-box; margin: 0; padding: 0; }
  html, body { width: 1200px; height: 933px; overflow: hidden; }
  body { background: var(--frame); font-family: "Arimo", Arial, sans-serif; color: var(--text); }

  .canvas { position: relative; width: 1200px; height: 933px; background: var(--frame); }
  .edge { position: absolute; left: 11px; top: 11px; width: 1178px; height: 911px; background: var(--frame-edge); border-radius: 3px; }
  .brochure { position: absolute; left: 27px; top: 26px; width: 1147px; height: 879px; background: var(--panel); overflow: hidden; }

  .nav-band { position: absolute; left: 0; top: 0; width: 1147px; height: 109px; background: var(--panel-deep); }
  .tab { position: absolute; top: 0; height: 109px; width: 191px;
         background: linear-gradient(180deg, var(--tab-top), var(--tab-bottom)); padding: 38px 0 0 30px;
         font-family: "Open Sans", sans-serif; }
  .tab-title { font-size: 17px; font-weight: 600; letter-spacing: .2px; line-height: 1.05; }
  .tab-sub { font-size: 15px; font-weight: 400; color: var(--tab-sub); line-height: 1.1; }
  .tab-arrow { position: absolute; right: 9px; bottom: 6px; width: 14px; height: 14px; }
  .tab--about { left: 0; }
  .tab--contact { left: 379px; }
  .tab-rest { position: absolute; top: 0; height: 109px; background: linear-gradient(180deg, #525455, var(--panel-deep)); }

  .cover-title { position: absolute; left: 773px; top: 0; width: 374px; height: 109px; background: var(--panel-deep);
                 text-align: center; font-family: "Open Sans", sans-serif; color: var(--text-soft); padding-top: 20px; }
  .cover-title .kicker { font-size: 17px; font-weight: 600; line-height: 1.1; }
  .cover-title .main { font-size: 29px; font-weight: 700; line-height: 1.05; }
  .cover-title .tail { font-size: 19px; font-weight: 600; line-height: 1.1; }

  .heading { position: absolute; left: 26px; font-family: "Open Sans", sans-serif; font-weight: 300; font-size: 33px; color: var(--text); }
  .copy { position: absolute; left: 26px; width: 340px; font-size: 14.4px; line-height: 17.8px; color: var(--text-soft); }
  .copy strong { color: var(--text); }
  .heading--offer { top: 118px; }
  .copy--offer { top: 172px; }
  .heading--deliver { top: 638px; }
  .copy--deliver { top: 690px; }

  .photo { position: absolute; }
  .photo--meeting { left: 0; top: 370px; width: 379px; height: 252px;
                    background: linear-gradient(160deg, var(--photo-room-a), #8b949c 55%, var(--photo-room-b)); }
  .photo--winner { left: 773px; top: 109px; width: 374px; height: 513px;
                   background: linear-gradient(180deg, var(--photo-sky-a), #b7c0cb 55%, var(--photo-sky-b)); }

  .fold-rule { position: absolute; left: 0; top: 622px; width: 773px; height: 1px; background: var(--rule); }

  .help { position: absolute; left: 379px; top: 248px; width: 394px; text-align: center; font-family: "Open Sans", sans-serif; color: var(--text-soft); }
  .help .small { font-size: 14px; font-weight: 600; line-height: 1.2; }
  .help .big { font-size: 23.5px; font-weight: 600; line-height: 1.1; }
  .help .under { font-size: 16px; font-weight: 600; line-height: 1.2; }

  .contact-block { position: absolute; font-size: 14.4px; line-height: 17.8px; color: var(--text-soft); font-style: normal; }
  .contact-block dt { font-weight: 700; }
  .contact-block .row { display: flex; }
  .contact-block .label { width: 108px; }
  .contact-block a { color: var(--accent); text-decoration: underline; }
  .service { left: 441px; top: 401px; }
  .address { left: 462px; top: 702px; color: var(--text); }
  .address .company { color: var(--accent); font-weight: 700; }
  .address .gap { height: 17.8px; }
  .address .label { width: 100px; }

  .brand { position: absolute; left: 773px; top: 690px; width: 374px; text-align: center; font-family: "Open Sans", sans-serif; }
  .brand .name { font-size: 30px; font-weight: 700; letter-spacing: -.5px; line-height: 1.1; }
  .brand .line { margin-top: 16px; font-size: 29px; line-height: 1; letter-spacing: -.5px; }
  .brand .line b { font-weight: 700; }
  .brand .line span { font-weight: 300; }
  .brand .tag { font-size: 14.5px; color: var(--text-muted); letter-spacing: .3px; margin-top: 3px; }
</style>
</head>
<body>
<div class="canvas">
  <div class="edge"></div>
  <main class="brochure">

    <header class="nav-band">
      <div class="tab tab--about">
        <div class="tab-title">ABOUT US</div>
        <div class="tab-sub">about our company</div>
        <svg class="tab-arrow" viewBox="0 0 14 14"><path d="M2 2 L11 11 M11 4 V11 H4" stroke="#8a8b8c" stroke-width="2" fill="none"/></svg>
      </div>
      <div class="tab-rest" style="left:191px;width:188px"></div>
      <div class="tab tab--contact">
        <div class="tab-title">CONTACT US</div>
        <div class="tab-sub">contact information</div>
        <svg class="tab-arrow" viewBox="0 0 14 14"><path d="M2 2 L11 11 M11 4 V11 H4" stroke="#8a8b8c" stroke-width="2" fill="none"/></svg>
      </div>
      <div class="tab-rest" style="left:570px;width:203px"></div>
      <div class="cover-title">
        <div class="kicker">PROFESSIONAL</div>
        <div class="main">MANAGEMENT</div>
        <div class="tail">SKILLS TRAINING</div>
      </div>
    </header>

    <h2 class="heading heading--offer">What we offer</h2>
    <p class="copy copy--offer"><strong>Quisque nulla.</strong> Lorem ipsum dolor sit amet, con-sectetur adipisicing elit, sed do eiusmod tempor incididunt ut labore et dolore magna aliqua. Ut enim ad minim veniam, quis nostrud exercitation ullamco laboris nisi ut aliquip ex ea commodo consequat. Duis aute irure dolor in reprehenderit in voluptate velit esse cillum dolore eu fugiat nulla pariatur. Excepteur sint occaecat cupidatat non proident, sunt in culpa qui officia deserunt mollit anim id est laborum</p>

    <div class="photo photo--meeting" role="img" aria-label="Photo of a trainer presenting at a flip chart to a team seated around a meeting table"></div>

    <section class="help">
      <div class="small">HAVE</div>
      <div class="big">QUESTIONS OR CONCERNS ?</div>
      <div class="under">WE'RE HERE TO HELP</div>
    </section>

    <dl class="contact-block service">
      <dt>Customer Service:</dt>
      <dd class="row"><span class="label">Telephone&nbsp;&nbsp;:</span><span>+0 000 000 000</span></dd>
      <dd class="row"><span class="label">FAX&nbsp;&nbsp;&nbsp;&nbsp;&nbsp;&nbsp;&nbsp;&nbsp;&nbsp;&nbsp;&nbsp;&nbsp;:</span><span>+0 000 000 000</span></dd>
      <dd>E-mail: <a>customers@companyname.com</a></dd>
    </dl>

    <div class="photo photo--winner" role="img" aria-label="Photo of a businessman leaping through a finish-line ribbon against the sky"></div>

    <div class="fold-rule"></div>

    <h2 class="heading heading--deliver">What we deliver</h2>
    <p class="copy copy--deliver"><strong>Quisque nulla.</strong> Lorem ipsum dolor sit amet, con-sectetur adipisicing elit, sed do eiusmod tempor incididunt ut labore et dolore magna aliqua. Ut enim ad minim veniam, quis nostrud exercitation ullamco laboris nisi ut aliquip ex ea commodo consequat. Duis aute irure dolor in reprehenderit in voluptate velit esse cillum dolore eu fugiat nulla pariatur. Excepteur sint occaecat cupidatat non proident, sunt in culpa qui officia deserunt mollit anim id est laborum</p>

    <address class="contact-block address">
      <div class="company">Your Company Name Inc.</div>
      <div>Street Address,</div>
      <div>State, Country, ZIP</div>
      <div class="gap"></div>
      <div class="row"><span class="label">Telephone&nbsp;&nbsp;:</span><span>+0 000 000 000</span></div>
      <div class="row"><span class="label">Fax.&nbsp;&nbsp;&nbsp;&nbsp;&nbsp;&nbsp;&nbsp;&nbsp;&nbsp;&nbsp;&nbsp;:</span><span>+0 000 000 000</span></div>
    </address>

    <div class="brand">
      <div class="name">YOUR COMPANY</div>
      <div class="line"><b>CORPORATE</b> <span>TRAINING</span></div>
      <div class="tag">THE BEST CORPORATE TRAINING CENTER</div>
    </div>

  </main>
</div>
</body>
</html>
```